Postcard Design to introduce Brightfold Utility Partners services

Company name: Indoor Water ConservationCustom fitted products for sinks, showers and toilets.Average savings 20%ROI 6 to 12 monthsNote: we just joined this organization and want to use this postcard to "introduce" our Company and services so that when they think of conserving water indoors, they think of use. In your images section are our logo (we have other resolutions if needed) and an image - we are open to suggestions for design and what to include.One suggestion is to introduce us and use the New Years Resolution - even if conserving water and saving money are not our new year's resolution, when you are ready to conserve water and save money, think of us.

Target Market(s)

2 markets - 1) hotels and 2) apartment complexes. 2 markets, 2 postcards, 2 mailing lists

Industry/Entity Type

It Company

Colors
85acd3
33a6d7
33b8a4

Requirements
Must have
• logo, company name, ave savings 20%, ROI 6 - 12 months, introduction that we are new service provider to 1) Pacific Guesthouse and Innkeepers Guild (1 mailing/1 postcard) and new service provider to 2) Western Rental Dwellers League (2nd mailing/2nd postcard).
Nice to have
• Using the concept of New Year's resolution, maybe a finger with a string tied to it about to turn off a faucet - or some similar image.

```html
<!DOCTYPE html>
<html lang="en">
<head>
<meta charset="utf-8">
<title>Brightfold Utility Partners – Postcard</title>
<link rel="stylesheet" href="https://fonts.googleapis.com/css2?family=Exo+2:wght@400;500;600&family=Lato:ital,wght@0,400;1,400&display=swap">
<style>
  :root {
    --ink-dark: #434343;
    --ink-text: #2b2b2b;
    --brand-blue: #1b7fc5;
    --sky-blue: #33a6d7;
    --soft-blue: #5db9e7;
    --pale-blue: #85acd3;
    --line-grey: #555555;
    --stamp-grey: #d8d8d8;
    --page-bg: #e6e6e6;
    --white: #ffffff;
  }
  * { margin: 0; padding: 0; box-sizing: border-box; }
  html, body { width: 825px; height: 1200px; overflow: hidden; }
  body { background: var(--page-bg); position: relative; font-family: "Exo 2", sans-serif; }

  .postcard { position: absolute; left: 87px; width: 653px; background: var(--white); overflow: hidden; }
  .postcard--front { top: 70px; height: 506px; }
  .postcard--back { top: 623px; height: 507px; }
  .postcard__shapes { position: absolute; inset: 0; }

  .photo-circle { position: absolute; border-radius: 50%; border: 5px solid var(--soft-blue); }
  .photo-circle--faucet { left: 28px; top: 162px; width: 140px; height: 140px;
    background: radial-gradient(circle at 45% 40%, #ffffff, #b9d3e6 55%, #6d95b8); }
  .photo-circle--shower { left: 173px; top: 177px; width: 110px; height: 110px;
    background: radial-gradient(circle at 55% 50%, #ffffff, #c7dbe9 55%, #7ea3c2); }
  .photo-circle--drops { left: 272px; top: 160px; width: 152px; height: 152px; border: 6px solid var(--brand-blue);
    background: radial-gradient(circle at 50% 50%, #6f7780, #2e3237 70%); }
  .photo-circle--glass { left: 246px; top: 274px; width: 104px; height: 104px; border: 5px solid var(--brand-blue);
    background: radial-gradient(circle at 50% 45%, #f2f5f7, #a9b4bd 70%); }

  .headline { position: absolute; line-height: 1; font-weight: 500; }
  .headline__top { display: block; color: var(--white); }
  .postcard--front .headline { left: 26px; top: 37px; }
  .postcard--front .headline__top { font-size: 39px; letter-spacing: 1px; }
  .postcard--front .headline__bottom { display: block; font-size: 27px; color: var(--soft-blue); margin-top: 4px; }
  .postcard--back .headline { left: 26px; top: 206px; }
  .postcard--back .headline__top { font-size: 41px; letter-spacing: 1px; }
  .postcard--back .headline__bottom { display: block; font-size: 27px; color: var(--ink-text); margin-top: 3px; font-weight: 600; }

  .roi { position: absolute; left: 244px; top: 302px; font-size: 31px; font-weight: 500; color: var(--brand-blue); letter-spacing: .3px; }
  .products { position: absolute; left: 218px; top: 350px; width: 435px; height: 35px; line-height: 33px; padding-left: 22px;
    font-size: 15.5px; color: var(--white); }
  .brand-name { position: absolute; left: 24px; top: 348px; width: 180px; display: flex; align-items: center; gap: 8px;
    font-size: 16px; font-weight: 600; color: var(--brand-blue); line-height: 1.1; }
  .brand-name__dot { flex: none; width: 26px; height: 26px; border-radius: 50%; background: var(--sky-blue); }
  .resolution { position: absolute; left: 206px; top: 400px; width: 420px; text-align: right;
    font-family: "Lato", sans-serif; font-style: italic; font-size: 13.2px; line-height: 17px; color: var(--ink-text); }

  .footer { position: absolute; left: 0; right: 0; bottom: 0; height: 46px; background: var(--brand-blue);
    color: var(--white); font-size: 15px; letter-spacing: 2.6px; line-height: 46px; text-align: center; }
  .footer-rule { position: absolute; left: 0; right: 0; bottom: 52px; height: 3px; background: var(--line-grey); }

  .intro { position: absolute; left: 30px; top: 36px; width: 312px; color: var(--white); font-size: 14.8px; line-height: 19.8px; }
  .stamp { position: absolute; left: 545px; top: 27px; width: 82px; height: 82px; background: var(--stamp-grey); }
  .contact { position: absolute; left: 26px; top: 298px; color: var(--ink-text); font-size: 22px; line-height: 28px; }
  .contact__rule { position: absolute; left: 26px; top: 283px; width: 210px; height: 2px; background: var(--white); }
  .memberships { position: absolute; left: 24px; top: 402px; list-style: none; font-size: 14.8px; line-height: 18px; color: var(--ink-text); }
  .memberships li { display: flex; align-items: center; gap: 6px; }
  .memberships li::before { content: ""; width: 8px; height: 8px; border-radius: 50%; background: var(--brand-blue); }
</style>
</head>
<body>

<section class="postcard postcard--front">
  <svg class="postcard__shapes" width="653" height="506" viewBox="0 0 653 506">
    <defs>
      <linearGradient id="front-photo" x1="0" y1="0" x2="1" y2="1">
        <stop offset="0" stop-color="#f4f9fc"/><stop offset=".6" stop-color="#cfe4f1"/><stop offset="1" stop-color="#8fbad8"/>
      </linearGradient>
      <linearGradient id="front-lower" x1="0" y1="0" x2="0" y2="1">
        <stop offset="0" stop-color="#ffffff"/><stop offset="1" stop-color="#e9eef2"/>
      </linearGradient>
    </defs>
    <rect width="653" height="506" fill="url(#front-lower)"/>
    <path role="img" aria-label="Splashing water shaped as a dove beside hands holding a water globe of the Earth"
          d="M262,0 H653 V228 C560,268 420,262 300,222 C280,190 272,140 262,90 Z" fill="url(#front-photo)"/>
    <path d="M210,182 C320,236 480,276 653,226" fill="none" stroke="var(--sky-blue)" stroke-width="6"/>
    <path d="M230,198 C340,248 500,284 653,240" fill="none" stroke="var(--pale-blue)" stroke-width="2"/>
    <path d="M268,0 C296,50 292,120 250,145 C215,162 140,160 60,160 C30,162 10,168 0,172" fill="none" stroke="var(--soft-blue)" stroke-width="7"/>
    <path d="M0,0 H260 C286,46 282,112 240,134 C206,150 150,146 0,146 Z" fill="var(--ink-dark)"/>
  </svg>

  <div class="photo-circle photo-circle--faucet" role="img" aria-label="Chrome faucet running water"></div>
  <div class="photo-circle photo-circle--shower" role="img" aria-label="Shower head spraying water"></div>

  <h1 class="headline"><span class="headline__top">AVERAGE</span><span class="headline__bottom">SAVINGS 20%</span></h1>

  <p class="brand-name"><span class="brand-name__dot"></span>Brightfold Utility Partners</p>

  <h2 class="roi">ROI FOR 6 - 12 MONTHS</h2>
  <svg style="position:absolute;left:218px;top:350px" width="435" height="35"><rect x="1" y="1" width="440" height="33" rx="16" fill="var(--soft-blue)" stroke="var(--brand-blue)" stroke-width="2"/></svg>
  <p class="products">Custom fitted products for sinks, showers and toilets</p>

  <p class="resolution">Even if conserving water and saving money are not our new year's resolu-<br>tion, when you are ready to conserve water and save money, think of us.</p>

  <div class="footer-rule"></div>
  <p class="footer">Please visit us to know more about us at - www.website.com</p>
</section>

<section class="postcard postcard--back">
  <svg class="postcard__shapes" width="653" height="507" viewBox="0 0 653 507">
    <defs>
      <linearGradient id="back-photo" x1="0" y1="0" x2="1" y2="1">
        <stop offset="0" stop-color="#f3f4f5"/><stop offset=".7" stop-color="#e4e8eb"/><stop offset="1" stop-color="#d3dbe1"/>
      </linearGradient>
    </defs>
    <rect role="img" aria-label="Soft water splash backdrop" width="653" height="507" fill="url(#back-photo)"/>
    <path d="M0,0 H360 C380,50 386,120 372,174 C348,262 322,320 336,372 V452 H0 Z" fill="var(--white)"/>
    <path d="M0,0 H356 C376,50 380,120 368,174 H0 Z" fill="var(--ink-dark)"/>
    <path d="M0,174 H368 C344,262 318,320 330,372 H0 Z" fill="var(--soft-blue)"/>
    <path d="M362,0 C384,56 388,130 372,196 C350,280 318,350 346,452" fill="none" stroke="var(--brand-blue)" stroke-width="6"/>
    <rect x="0" y="372" width="335" height="4" fill="var(--brand-blue)"/>
  </svg>

  <p class="intro">Lorem ipsum dolor sit amet, consectetuer adipiscing elit, sed diam nonummy nibh euismod tincidunt ut laoreet dolore magna aliquam erat volutpat.Lorem ipsum dolor sit amet, consectetuer adipiscing elitpat.</p>
  <div class="stamp" aria-hidden="true"></div>

  <div class="photo-circle photo-circle--drops" role="img" aria-label="Water droplets falling from a rain shower"></div>
  <div class="photo-circle photo-circle--glass" role="img" aria-label="Glass being filled at a tap"></div>

  <h2 class="headline"><span class="headline__top">AVERAGE</span><span class="headline__bottom">SAVINGS 20%</span></h2>
  <div class="contact__rule"></div>
  <p class="contact">Contact us now at:<br>123.456.789</p>

  <ul class="memberships">
    <li>Pacific Guesthouse and Innkeepers Guild</li>
    <li>Western Rental Dwellers League</li>
  </ul>

  <div class="footer-rule"></div>
  <p class="footer">Please visit us to know more about us at - www.website.com</p>
</section>

</body>
</html>
```